Personal Trainer and Corporate Health Business

I need a business card for a new company I'm starting in Australia called "Brisk Vigour Outreach" I will be providing a Personal training service as well as corporate health in companies.
The service provided is to help promote an active and healthy lifstyle.
The design should communicate a healthy lifestyle and also the benefits that this can have on a personal level and in the corporate environment and the benefits that flow from that.

Target Market(s)

Members of the public and Corporate

Industry/Entity Type

Environment

Requirements
Must have
• Company logo attached
Look and feel fresh and modern

Tag line: "Actively promoting a healthier lifestyle"

Colin Varga
Managing Director

m: 0412 657 394
e: colin@briskvigouroutreach.com.au

www.briskvigouroutreach.com.au
Nice to have
• Can be 1 or 2 sided

```html
<!DOCTYPE html>
<html lang="en">
<head>
<meta charset="utf-8">
<title>Brisk Vigour Outreach – Business Card</title>
<link rel="stylesheet" href="https://fonts.googleapis.com/css2?family=Libre+Baskerville:ital,wght@0,400;0,700;1,400&display=swap">
<style>
  :root {
    --brand-blue: #0561ad;
    --brand-green: #a3cb38;
    --card-white: #ffffff;
    --backdrop: #ecece8;
    --card-shadow: rgba(0, 0, 0, 0.28);
  }
  html, body {
    margin: 0;
    padding: 0;
    width: 1200px;
    height: 1000px;
    overflow: hidden;
    background: var(--backdrop);
  }
  .canvas {
    position: relative;
    width: 1200px;
    height: 1000px;
    font-family: "Libre Baskerville", "Palatino Linotype", serif;
  }
  .card {
    position: absolute;
    background: var(--card-white);
    box-shadow: 2px 6px 14px var(--card-shadow);
    overflow: hidden;
  }
  .card svg { display: block; }
  .card-back { left: 94px; top: 455px; width: 728px; height: 415px; }
  .card-front { left: 304px; top: 112px; width: 729px; height: 418px; }
  .band-green { fill: var(--brand-green); }
  .band-blue { fill: var(--brand-blue); }
  .person-name { fill: var(--brand-blue); font-weight: 700; font-size: 27px; letter-spacing: 0.3px; }
  .person-role { fill: var(--brand-green); font-size: 14.5px; }
  .contact-line { fill: var(--brand-blue); font-size: 13px; letter-spacing: 0.6px; }
  .icon-tile { fill: var(--brand-green); }
  .icon-glyph { fill: none; stroke: var(--card-white); stroke-width: 1.4; }
  .tagline { fill: var(--brand-blue); font-style: italic; font-size: 17px; letter-spacing: 0.4px; }
  .tagline-accent { fill: var(--brand-green); }
  .brand-name { fill: var(--brand-blue); font-weight: 700; font-size: 26px; letter-spacing: 0.5px; }
  .brand-dot { fill: var(--brand-green); }
</style>
</head>
<body>
<main class="canvas">

  <section class="card card-back" aria-label="Card back">
    <svg width="728" height="415" viewBox="0 0 728 415">
      <path class="band-green" d="M0 176 C40 300 330 398 728 273 L728 415 L0 415 Z"/>
      <path class="band-blue" d="M0 186 C70 330 330 392 728 310 L728 415 L0 415 Z"/>
      <circle class="brand-dot" cx="363" cy="162" r="9"/>
      <text class="brand-name" x="363" y="210" text-anchor="middle">Brisk Vigour</text>
      <text class="brand-name" x="363" y="244" text-anchor="middle">Outreach</text>
    </svg>
  </section>

  <section class="card card-front" aria-label="Card front">
    <svg width="729" height="418" viewBox="0 0 729 418">
      <defs>
        <path id="tagline-curve" d="M380 332 Q565 298 704 188"/>
      </defs>
      <path class="band-green" d="M0 278 C230 380 540 400 729 178 L729 418 L0 418 Z"/>
      <path class="band-blue" d="M0 312 C240 404 560 414 729 206 L729 418 L0 418 Z"/>

      <text class="person-name" x="34" y="70">COLIN VARGA</text>
      <text class="person-role" x="34" y="92">Managing Director</text>

      <g class="contact-phone">
        <rect class="icon-tile" x="33" y="170" width="21" height="21" rx="4"/>
        <rect class="icon-glyph" x="39" y="174" width="9" height="13" rx="1.5"/>
        <text class="contact-line" x="65" y="186">0412 657 394</text>
      </g>
      <g class="contact-email">
        <rect class="icon-tile" x="33" y="201" width="21" height="21" rx="4"/>
        <rect class="icon-glyph" x="37" y="206" width="13" height="10"/>
        <path class="icon-glyph" d="M37 206 L43.5 212 L50 206"/>
        <text class="contact-line" x="65" y="217">colin@briskvigouroutreach.com.au</text>
      </g>
      <g class="contact-web">
        <rect class="icon-tile" x="33" y="234" width="21" height="21" rx="4"/>
        <circle class="icon-glyph" cx="43.5" cy="244.5" r="6.5"/>
        <path class="icon-glyph" d="M37 244.5 H50 M43.5 238 V251"/>
        <text class="contact-line" x="67" y="250">www.briskvigouroutreach.com.au</text>
      </g>

      <text class="tagline">
        <textPath href="#tagline-curve">Actively promoting a <tspan class="tagline-accent">healthier</tspan> lifestyle</textPath>
      </text>
    </svg>
  </section>

</main>
</body>
</html>
```